Yard sign design for high end luxury home builder.

Need a design for signage on custom homes that are being built. I already have a logo that I am satisfied with that needs to be incorporated. I need the following incorporated in the design of the sign-
- Lic number 318562
- phone number (555) 271-4038
- pendrickhomeworks.com
- Logo/Branding

If possible it may be nice to have the following quote that is on are business cards-

Quote from Osmund of Veltarra-
HE WHO WORKS WITH HIS HANDS IS A LABORER.
HE WHO WORKS WITH HIS HANDS & HIS HEAD IS A CRAFTSMAN.
HE WHO WORKS WITH HIS HANDS & HIS HEAD & HIS HEART IS AN ARTISAN.
-OSMUND OF VELTARRA

Target Market(s)

Archetect, Designers, Clients desiring to build a new home or remodel.

Colors
fde9d4
fee4d5
fabb94
fac994
faa54b
f68d4d
f37122
f78f20
f68e4e

Requirements
Must have
• - Lic number 318562
• - phone number (555) 271-4038
• - pendrickhomeworks.com
• - Logo/Branding
Nice to have
• Quote from Osmund of Veltarra-
• HE WHO WORKS WITH HIS HANDS IS A LABORER.
• HE WHO WORKS WITH HIS HANDS & HIS HEAD IS A CRAFTSMAN.
• HE WHO WORKS WITH HIS HANDS & HIS HEAD & HIS HEART IS AN ARTISAN.
• -OSMUND OF VELTARRA
• OR the below statement-
• Craftsmen that Care
Should not have
• Any additional verbiage not specified above including any type of verbiage about what kind of company we are. For instance- Integrity, reputable... It's just all played out. Im just looking for a bitching design that has the info that compliments my logo/branding.

```html
<!DOCTYPE html>
<html lang="en">
<head>
<meta charset="utf-8">
<title>Pendrick Homeworks Yard Sign</title>
<link rel="stylesheet" href="https://fonts.googleapis.com/css2?family=Exo+2:wght@700;800&family=Michroma&family=Open+Sans:wght@400;700&display=swap">
<style>
  :root {
    --page-bg: #e9e7e3;
    --sign-white: #fbfbfa;
    --sign-dark: #2a2a2a;
    --accent-orange: #f37122;
    --ink: #111111;
    --brand-brown: #6b5442;
    --quote-text: #e8e8e8;
  }
  * { margin: 0; padding: 0; box-sizing: border-box; }
  html, body {
    width: 1200px;
    height: 1200px;
    overflow: hidden;
    background: var(--page-bg);
  }
  .yard-sign {
    position: absolute;
    left: 195px;
    top: 60px;
    width: 810px;
    height: 1080px;
    background: var(--sign-white);
    box-shadow: 0 10px 30px rgba(0,0,0,0.18);
    overflow: hidden;
  }
  .sign-base {
    position: absolute;
    left: 0; top: 0;
    width: 810px; height: 1080px;
  }
  .brand {
    position: absolute;
    top: 120px;
    left: 0;
    width: 100%;
    display: flex;
    justify-content: center;
    align-items: center;
    gap: 18px;
  }
  .brand-square {
    width: 64px;
    height: 64px;
    background: var(--brand-brown);
  }
  .brand-name {
    font-family: "Michroma", sans-serif;
    font-size: 34px;
    color: var(--brand-brown);
    letter-spacing: 2px;
    line-height: 1.1;
  }
  .contact-line {
    position: absolute;
    top: 312px;
    left: 0;
    width: 100%;
    text-align: center;
    font-family: "Exo 2", sans-serif;
    font-weight: 800;
    font-size: 50px;
    color: var(--ink);
    white-space: nowrap;
  }
  .contact-line .phone { color: var(--accent-orange); }
  .license-pill {
    position: absolute;
    top: 391px;
    left: 277px;
    width: 236px;
    height: 30px;
    border-radius: 15px;
    background: var(--ink);
    color: #ffffff;
    font-family: "Open Sans", sans-serif;
    font-weight: 700;
    font-size: 19px;
    line-height: 30px;
    text-align: center;
  }
  .quote-block {
    position: absolute;
    top: 616px;
    left: 40px;
    width: 730px;
    text-align: center;
    font-family: "Open Sans", sans-serif;
    color: var(--quote-text);
  }
  .quote-rule {
    display: flex;
    justify-content: center;
    align-items: center;
    gap: 14px;
    height: 30px;
  }
  .quote-rule .line {
    width: 150px;
    height: 2px;
    background: var(--accent-orange);
  }
  .quote-rule .mark {
    font-family: "Exo 2", sans-serif;
    font-weight: 800;
    font-style: normal;
    font-size: 40px;
    line-height: 30px;
    color: var(--quote-text);
    padding-top: 12px;
  }
  .quote-lines { margin: 18px 0 16px; }
  .quote-lines p {
    font-size: 28px;
    line-height: 42px;
    margin-bottom: 8px;
  }
  .attribution {
    position: absolute;
    top: 936px;
    right: 55px;
    font-family: "Open Sans", sans-serif;
    font-weight: 700;
    font-size: 26px;
    color: #ffffff;
  }
  .website {
    position: absolute;
    top: 1028px;
    left: 0;
    width: 100%;
    text-align: center;
    font-family: "Open Sans", sans-serif;
    font-size: 19px;
    letter-spacing: 8px;
    color: #f2f2f2;
  }
</style>
</head>
<body>
  <div class="yard-sign">
    <svg class="sign-base" viewBox="0 0 810 1080" aria-hidden="true">
      <polygon points="0,608 402,450 810,630 810,1080 0,1080" fill="var(--sign-dark)"/>
      <polyline points="0,598 402,440 810,620" fill="none" stroke="var(--accent-orange)" stroke-width="18"/>
    </svg>

    <div class="brand">
      <div class="brand-square"></div>
      <div class="brand-name">PENDRICK<br>HOMEWORKS</div>
    </div>

    <div class="contact-line">Contact us:<span class="phone">(555) 271-4038</span></div>
    <div class="license-pill">LIC NUMBER 318562</div>

    <div class="quote-block">
      <div class="quote-rule"><span class="line"></span><span class="mark">&#8220;</span><span class="line"></span></div>
      <div class="quote-lines">
        <p>He who works with his hands is a LABORER.</p>
        <p>He who works with his hands and head is a<br>CRAFTSMAN</p>
        <p>He who works with his hands and head and his<br>heart is an ARTISAN.</p>
      </div>
      <div class="quote-rule"><span class="line"></span><span class="mark">&#8221;</span><span class="line"></span></div>
    </div>

    <div class="attribution">- OSMUND OF VELTARRA</div>
    <div class="website">PENDRICKHOMEWORKS.COM</div>
  </div>
</body>
</html>
```